Poster for a Vegetarian Food Truck/Restaurant

Ours is a food truck with lots of greens in the menu. The name of our restaurant is Plum Nibbles.

I want to create a Poster image for the restaurant. Please submit designs on any one or both the themes described below

Size: 1.6 meters by 4.6 meters (horizontal)

Design Theme #1
A poster based off 'Newspaper front page'.
The poster should look like the front page of a newspaper with 'Plum Nibbles' as its name. The Plum Nibbles should appear prominently (in green color, possibly light green or lemon color). The poster will have a few snippets about benefits of certain food items or some trivia along with an image. For example 'Garlic is high in minerals & vitamins', 'Chickpeas are high on fiber'. I'll decide on the exact text meanwhile.

I have attached 2 sample images to give an idea.

Design Theme #2

It should consist of the following 3 components:
1. Green Forest like back ground
2. Image of a chef with a welcoming, smiling face
3. The text 'Plum Nibbles' should appear in the poster

I want Tobin Marsh lookalike, the main character from the animation movie 'Sunny Days over Dumpling Hill' to be the chef placed in the poster.
The chef should appear confident, smiling, young with his typical hair style

A sample picture of tobin marsh is attached in the brief

Target Market(s)

The poster will be pasted on a food truck

Industry/Entity Type

Restaurant

Requirements
Must have
• Poster with light but high resolution image(s)
• Attention to detail
Should not have
• The poster should not have dense/dark colors

```html
<!DOCTYPE html>
<html lang="en">
<head>
<meta charset="utf-8">
<title>Plum Nibbles Poster</title>
<link rel="stylesheet" href="https://fonts.googleapis.com/css2?family=Bebas+Neue&family=Courgette&family=Crimson+Text:ital,wght@0,600;1,600&family=Josefin+Sans:wght@600&family=Amatic+SC:wght@700&family=Parisienne&family=Lora:ital,wght@1,700&display=swap">
<style>
:root{
  --page:#efefef;
  --paper:#ffffff;
  --khaki:#c6c991;
  --lime-pale:#eaf6a3;
  --lime:#bdd236;
  --leaf:#8fb42f;
  --sky:#a7c7d5;
  --sage:#9cc27f;
  --olive:#6a6a2a;
  --olive-soft:#b3aa70;
  --brown:#6d6238;
  --ink:#555555;
  --white:#ffffff;
}
*{margin:0;padding:0;box-sizing:border-box}
html,body{width:1200px;height:848px;overflow:hidden;background:var(--page)}
.poster{position:absolute;left:36px;top:222px;width:1128px;height:404px;background:var(--paper)}
.block{position:absolute}
.photo{position:absolute}
.chickpea-panel{left:10px;top:11px;width:194px;height:381px;background:var(--khaki)}
.chickpea-photo{left:19px;top:20px;width:155px;height:147px;background:radial-gradient(circle at 50% 55%,#d8d8d8,#a9a9a9 70%,#efefef)}
.chickpea-text{position:absolute;left:0;top:180px;width:194px;text-align:center;font-family:"Courgette",cursive;font-size:29px;line-height:49px;color:var(--white)}
.lime-note{left:214px;top:13px;width:127px;height:247px;background:var(--lime-pale);border-radius:8px;display:flex;align-items:center;justify-content:center;text-align:center;font-family:"Crimson Text",serif;font-style:italic;font-weight:600;font-size:21px;line-height:36.5px;color:var(--olive)}
.lime-photo{left:216px;top:275px;width:126px;height:118px;border-radius:50%;background:radial-gradient(circle,#eef7a0 0%,#c2dc48 55%,#7ea92a 100%)}
.avocado-photo{left:359px;top:14px;width:98px;height:126px;border-radius:45% 45% 40% 40%;background:radial-gradient(circle at 62% 60%,#e8f08a 0%,#b6c84a 35%,#3f4a1c 80%)}
.avocado-kicker{position:absolute;left:464px;top:23px;font-family:"Josefin Sans",sans-serif;font-weight:600;font-size:19px;letter-spacing:2px;color:var(--brown)}
.avocado-title{position:absolute;left:495px;top:48px;font-family:"Josefin Sans",sans-serif;font-weight:600;font-size:20px;letter-spacing:2.6px;color:var(--brown)}
.avocado-bar{left:513px;top:16px;width:262px;height:24px;border-radius:6px;background:var(--lime-pale)}
.avocado-tag{left:513px;top:76px;width:262px;height:78px;border-radius:6px;background:var(--leaf);display:flex;flex-direction:column;justify-content:center;align-items:center;font-family:"Amatic SC",sans-serif;font-weight:700;font-size:22px;letter-spacing:10px;line-height:32px;color:var(--white)}
.brand{left:353px;top:167px;width:422px;height:108px;border-radius:8px;background:var(--lime);display:flex;align-items:center;justify-content:center;font-family:"Bebas Neue",sans-serif;font-size:86px;letter-spacing:2px;color:var(--white);padding-top:6px}
.cucumber-note{left:353px;top:289px;width:323px;height:103px;background:var(--sky);display:flex;align-items:center;justify-content:center;text-align:center;font-family:"Parisienne",cursive;font-size:29px;line-height:36px;color:var(--white)}
.cucumber-photo{left:686px;top:306px;width:90px;height:67px;border-radius:50%;background:radial-gradient(circle,#e4f2b4 0%,#a9d06a 55%,#4f8a2a 100%)}
.garlic-photo{left:790px;top:31px;width:154px;height:107px;border-radius:48%;background:radial-gradient(circle at 45% 55%,#fafafa,#cfcfcf 60%,#ffffff)}
.garlic-note{left:788px;top:156px;width:158px;height:236px;border-radius:8px;background:var(--lime-pale);text-align:center;font-family:"Crimson Text",serif;font-weight:600;text-transform:uppercase;color:var(--olive);padding-top:6px}
.garlic-note .lg{display:block;font-size:33px;line-height:38px;color:var(--olive-soft)}
.garlic-note .md{display:block;font-size:31px;line-height:36px}
.garlic-note .wide{display:block;font-size:38px;line-height:40px;color:var(--olive-soft);letter-spacing:14px;padding-left:14px;transform:scaleY(.55)}
.garlic-note .sm{display:block;font-size:21px;line-height:30px}
.garlic-note .amp{display:block;font-size:26px;line-height:30px;color:var(--olive-soft)}
.leaf-stripes{left:960px;top:11px;width:38px;height:144px}
.leaf-panel{left:998px;top:11px;width:116px;height:144px;background:var(--sage);padding:12px 12px 0 0;text-align:right;font-family:"Lora",serif;font-style:italic;font-weight:700;font-size:27px;line-height:41px;color:var(--white)}
.leaf-label{position:absolute;left:960px;top:167px;width:154px;display:flex;justify-content:space-between;font-family:"Josefin Sans",sans-serif;font-weight:600;font-size:7px;letter-spacing:3px;color:var(--ink)}
.leaf-photo{left:960px;top:187px;width:154px;height:205px;background:radial-gradient(circle at 40% 40%,#e8f59a 0%,#a6cf3c 45%,#4f8a1e 100%)}
</style>
</head>
<body>
<main class="poster">
  <section class="block chickpea-panel">
    <div class="photo chickpea-photo" role="img" aria-label="Bowls of chickpeas, black and white photo"></div>
    <p class="chickpea-text">Chickpeas<br>are<br>high<br>on fiber</p>
  </section>

  <p class="block lime-note">Lime is<br>high in<br>vitamin C<br>and it<br>improves<br>digestion</p>
  <div class="photo lime-photo" role="img" aria-label="Halved lime photo"></div>

  <div class="photo avocado-photo" role="img" aria-label="Whole and halved avocado photo"></div>
  <div class="block avocado-bar"></div>
  <p class="avocado-kicker">THE</p>
  <h2 class="avocado-title">AMAZING AVOCADO</h2>
  <p class="block avocado-tag"><span>RICH,CREAMY</span><span>&amp; FLAVORFUL</span></p>

  <h1 class="block brand">Plum Nibbles</h1>

  <p class="block cucumber-note">Cucumbers are usually<br>more than 90% water.</p>
  <div class="photo cucumber-photo" role="img" aria-label="Cucumber slices photo"></div>

  <div class="photo garlic-photo" role="img" aria-label="Garlic bulbs and cloves, black and white photo"></div>
  <p class="block garlic-note">
    <span class="lg">Garlic</span>
    <span class="md">is high</span>
    <span class="wide">in</span>
    <span class="sm">Minerals</span>
    <span class="amp">&amp;</span>
    <span class="sm">Vitamins</span>
  </p>

  <svg class="block leaf-stripes" viewBox="0 0 38 144" aria-hidden="true">
    <rect width="38" height="144" fill="#ffffff"/>
    <rect x="3" width="3" height="144" fill="#9cc27f"/>
    <rect x="10" width="3" height="144" fill="#9cc27f"/>
    <rect x="17" width="3" height="144" fill="#9cc27f"/>
    <rect x="24" width="3" height="144" fill="#9cc27f"/>
    <rect x="31" width="7" height="144" fill="#9cc27f"/>
  </svg>
  <p class="block leaf-panel">Raw<br>green<br>leaf</p>
  <p class="leaf-label"><span>THE</span><span>BENEFITS</span></p>
  <div class="photo leaf-photo" role="img" aria-label="Fresh frilly green lettuce leaves photo"></div>
</main>
</body>
</html>
```